Home Security Company Business Card

Looking for a eye catching business card that is non traditional and stands out but yet still looks professional. It should include all the pertinent information such as name, title, address, telephone, e-mail, website address should definitely stand out and then finally the logo.

Target Market(s)

Residential and Commercial accounts mostly upscale accounts

Industry/Entity Type

Security

Contact Information for Business Card

Name
Title
Address
Office #
Cell #
E-mail
Website

Font styles to use
Serif
Sans Serif

Requirements
Must have
• Logo, two sided color configuration
Nice to have
• You decide
Should not have
• There really aren't any.

```html
<!DOCTYPE html>
<html lang="en">
<head>
<meta charset="utf-8">
<title>Ironvale Security Systems – Business Card</title>
<link rel="stylesheet" href="https://fonts.googleapis.com/css2?family=Mulish:wght@400;500&display=swap">
<style>
  :root {
    --backdrop: #d3d3d3;
    --card: #f7f7f6;
    --ink: #1c1c1c;
    --ink-soft: #3a3a3a;
    --rule: #c9c9c9;
    --gold: #ecbf3a;
    --crimson: #b2241a;
  }
  * { box-sizing: border-box; margin: 0; padding: 0; }
  html, body {
    width: 1200px; height: 900px; overflow: hidden;
    background: var(--backdrop);
  }
  .canvas {
    width: 1200px; height: 900px;
    display: flex; flex-direction: column;
    align-items: center; justify-content: center; gap: 36px;
  }
  .card {
    position: relative;
    width: 700px; height: 400px;
    background: var(--card);
    overflow: hidden;
    box-shadow: 0 2px 6px rgba(0,0,0,.12);
    font-family: "Mulish", sans-serif;
  }
  .card__art { position: absolute; inset: 0; width: 100%; height: 100%; }

  /* Front: contact block */
  .contact {
    position: absolute; left: 27px; top: 122px; width: 240px;
    text-align: center; color: var(--ink);
  }
  .contact__name { font-size: 34px; font-weight: 500; letter-spacing: .3px; line-height: 1.1; }
  .contact__title {
    font-size: 13px; letter-spacing: .6px; text-transform: uppercase;
    color: var(--ink-soft); margin-top: 10px; padding-bottom: 12px;
    border-bottom: 1px solid var(--rule);
  }
  .contact__details {
    list-style: none; margin-top: 12px; font-size: 16px; line-height: 1.38; white-space: nowrap;
  }

  /* Company name, set in the card's own text face */
  .brand {
    position: absolute; transform: translate(-50%, -50%);
    text-align: center; white-space: nowrap;
    color: var(--ink); font-weight: 500; line-height: 1.2;
  }
  .brand--front { left: 490px; top: 198px; }
  .brand__name { font-size: 30px; letter-spacing: .4px; }
  .brand__line { font-size: 15px; margin-top: 2px; letter-spacing: .4px; }

  .brand--back { left: 400px; top: 200px; }
  .brand--back .brand__name { font-size: 40px; }
  .brand--back .brand__line { font-size: 19px; margin-top: 4px; }
</style>
</head>
<body>
<main class="canvas">

  <section class="card card--front" aria-label="Business card front">
    <svg class="card__art" viewBox="0 0 700 400" aria-hidden="true">
      <path d="M433 0 C 345 110, 330 290, 383 400" fill="none" stroke="var(--crimson)" stroke-width="11"/>
      <circle cx="490" cy="198" r="188" fill="var(--card)"/>
      <circle cx="490" cy="198" r="188" fill="none" stroke="var(--gold)" stroke-width="4"/>
    </svg>

    <div class="contact">
      <h1 class="contact__name">Daniel Reyes</h1>
      <p class="contact__title">General Manager</p>
      <ul class="contact__details">
        <li>Cell: 123 456 789</li>
        <li>Office: 123 456 789</li>
        <li>danielreyes@ironvale.com</li>
        <li>ironvale.com</li>
        <li>Address Line 1, Address Line 2</li>
      </ul>
    </div>

    <div class="brand brand--front">
      <p class="brand__name">Ironvale</p>
      <p class="brand__line">Security Systems Inc.</p>
    </div>
  </section>

  <section class="card card--back" aria-label="Business card back">
    <svg class="card__art" viewBox="0 0 700 400" aria-hidden="true">
      <circle cx="400" cy="200" r="205" fill="none" stroke="var(--gold)" stroke-width="4"/>
    </svg>
    <div class="brand brand--back">
      <p class="brand__name">Ironvale</p>
      <p class="brand__line">Security Systems Inc.</p>
    </div>
  </section>

</main>
</body>
</html>
```